Corporate Business Card

Very professional, Modern, Not to busy, include phone address email, website
(509) 555-0174, 61807 19th Street N, Corvale, OR 98517, marcus@kestrelbayholding.com, brelvanindustries.com

Target Market(s)

Manufacturing

Industry/Entity Type

Aero, machining, manufacturing, Off road racing

Contact Information for Business Card

Phone, address email, website

```html
<!DOCTYPE html>
<html lang="en">
<head>
<meta charset="UTF-8">
<title>Brelvan Industries – Business Card</title>
<link href="https://fonts.googleapis.com/css2?family=Roboto:wght@400;500;700;900&display=swap" rel="stylesheet">
<style>
  :root {
    --navy: #16275f;
    --red: #d61f26;
    --paper: #ffffff;
    --backdrop: #c8c8c8;
    --ink: #1a1a1a;
    --quilt: #ececec;
    --icon-border: #b9bfd2;
  }
  * { margin: 0; padding: 0; box-sizing: border-box; }
  html, body { width: 1200px; height: 1200px; overflow: hidden; }
  body {
    background: var(--backdrop);
    font-family: "Roboto", Arial, sans-serif;
    position: relative;
  }
  .card {
    position: absolute;
    left: 250px;
    width: 700px;
    height: 400px;
    background: var(--paper);
    overflow: hidden;
    box-shadow: 0 10px 30px rgba(0,0,0,0.18);
  }
  .card--front { top: 150px; }
  .card--back { top: 640px; }

  .quilt-texture { position: absolute; }
  .card--front .quilt-texture {
    right: 0; top: 0; width: 360px; height: 330px;
    background: radial-gradient(ellipse at 85% 30%, var(--quilt) 0%, rgba(255,255,255,0) 70%);
  }
  .card--back .quilt-texture {
    left: 0; top: 127px; width: 340px; height: 273px;
    background: radial-gradient(ellipse at 20% 60%, var(--quilt) 0%, rgba(255,255,255,0) 70%);
  }

  /* Front */
  .brand {
    position: absolute;
    left: 110px;
    top: 105px;
    color: var(--navy);
    font-weight: 900;
  }
  .brand__name { font-size: 84px; line-height: 1; letter-spacing: -1px; display: block; }
  .brand__sub { font-size: 30px; display: block; text-align: right; margin-top: 6px; }
  .brand-rule {
    position: absolute;
    left: 110px; top: 262px;
    width: 240px; height: 3px;
    background: var(--navy);
  }
  .stripe { position: absolute; left: 0; width: 100%; }
  .stripe--red { top: 338px; height: 3px; background: var(--red); }
  .stripe--navy { top: 348px; height: 9px; background: var(--navy); }

  /* Back */
  .person {
    position: absolute;
    right: 50px; top: 34px;
    text-align: right;
    color: var(--navy);
  }
  .person__name { font-size: 34px; font-weight: 900; line-height: 1; }
  .person__title { font-size: 17px; color: var(--ink); margin-top: 6px; }
  .divider {
    position: absolute;
    left: 0; top: 125px;
    width: 100%; height: 2px;
    background: var(--red);
  }
  .contacts {
    position: absolute;
    right: 50px; top: 152px;
    list-style: none;
  }
  .contact {
    display: flex;
    align-items: center;
    justify-content: flex-end;
    gap: 16px;
    height: 46px;
    font-size: 19px;
    color: var(--ink);
  }
  .contact--phone { font-weight: 700; font-size: 20px; }
  .contact__icon {
    width: 34px; height: 34px;
    border: 1.5px solid var(--icon-border);
    display: flex; align-items: center; justify-content: center;
    background: var(--paper);
    flex-shrink: 0;
  }
  .contact__icon svg { width: 20px; height: 20px; }
</style>
</head>
<body>

  <section class="card card--front" aria-label="Business card front">
    <div class="quilt-texture" role="img" aria-label="Soft embossed quilted diamond texture"></div>
    <div class="brand">
      <span class="brand__name">BRELVAN</span>
      <span class="brand__sub">Industries</span>
    </div>
    <div class="brand-rule"></div>
    <div class="stripe stripe--red"></div>
    <div class="stripe stripe--navy"></div>
  </section>

  <section class="card card--back" aria-label="Business card back">
    <div class="quilt-texture" role="img" aria-label="Soft embossed quilted diamond texture"></div>
    <div class="person">
      <div class="person__name">YOUR NAME</div>
      <div class="person__title">Designation</div>
    </div>
    <div class="divider"></div>
    <ul class="contacts">
      <li class="contact contact--address">
        <span>61807 19th Street N, Corvale, OR 98517</span>
        <span class="contact__icon">
          <svg viewBox="0 0 24 24"><path fill="var(--red)" d="M12 2a7 7 0 0 0-7 7c0 5 7 13 7 13s7-8 7-13a7 7 0 0 0-7-7zm0 9.5A2.5 2.5 0 1 1 12 6.5a2.5 2.5 0 0 1 0 5z"/></svg>
        </span>
      </li>
      <li class="contact contact--phone">
        <span>(509) 555-0174</span>
        <span class="contact__icon">
          <svg viewBox="0 0 24 24"><path fill="var(--red)" d="M6.6 10.8a15 15 0 0 0 6.6 6.6l2.2-2.2c.3-.3.7-.4 1-.2 1.1.4 2.3.6 3.6.6.6 0 1 .4 1 1V20c0 .6-.4 1-1 1A17 17 0 0 1 3 4c0-.6.4-1 1-1h3.5c.6 0 1 .4 1 1 0 1.3.2 2.5.6 3.6.1.3 0 .7-.2 1z"/></svg>
        </span>
      </li>
      <li class="contact contact--email">
        <span>marcus@kestrelbayholding.com</span>
        <span class="contact__icon">
          <svg viewBox="0 0 24 24"><rect x="2" y="5" width="20" height="14" fill="var(--red)"/><path d="M2 5l10 8 10-8" fill="none" stroke="#fff" stroke-width="1.6"/></svg>
        </span>
      </li>
      <li class="contact contact--web">
        <span>brelvanindustries.com</span>
        <span class="contact__icon">
          <svg viewBox="0 0 24 24" fill="none" stroke="var(--red)" stroke-width="1.6"><circle cx="12" cy="12" r="9"/><ellipse cx="12" cy="12" rx="4" ry="9"/><path d="M3 12h18M5 7h14M5 17h14"/></svg>
        </span>
      </li>
    </ul>
  </section>

</body>
</html>
```